velvet dune glow beer

We are a small contract brewer looking to create a Glow Beer for upscale markets in Miami Beach and vicinity. We need a logo that reflects the aura of Velvet Dune: hip, healthy, exciting, sexy, etc. The logo needed will be used on our product ( i.e. bottle ) and along with the bottle's lettering, must encompass these qualities. Like Tin Lantern beer is synonymous with Jamaica, our goal is to be Miami Beach's official beer. We would like the logo and bottle to be modern in it's look, and have a distinct face with high visibility, easily recognizable sitting on a shelf.

Product name: VELVET DUNE GLOW

```html
<!DOCTYPE html>
<html lang="en">
<head>
<meta charset="utf-8">
<title>Velvet Dune Glow Beer — Label</title>
<link rel="stylesheet" href="https://fonts.googleapis.com/css2?family=Rubik:wght@700&display=swap">
<style>
  :root {
    --page: #ffffff;
    --band-teal: #2f6f78;
    --rim-light: #d6e4cc;
    --inner-rim: #f4e9b6;
    --sky-top: #f5ecb4;
    --sky-mid: #f0d38c;
    --town: #e6a866;
    --water: #4fa6a4;
    --water-deep: #3b8e93;
    --name-green: #5f7f1c;
    --strap-green: #a9cf5c;
    --strap-cream: #d5e6c6;
    --abv-red: #c2432b;
  }
  html, body {
    margin: 0;
    padding: 0;
    width: 739px;
    height: 1200px;
    overflow: hidden;
    background: var(--page);
  }
  .label {
    display: block;
    width: 739px;
    height: 1200px;
  }
  .band { fill: var(--band-teal); stroke: var(--rim-light); stroke-width: 6; }
  .scene-rim { fill: none; stroke: var(--inner-rim); stroke-width: 6; }
  .product-name {
    font-family: "Rubik", Arial, sans-serif;
    font-weight: 700;
    fill: var(--name-green);
  }
  .product-name--large { font-size: 104px; }
  .product-name--sub { font-size: 78px; }
  .abv {
    font-family: "Rubik", Arial, sans-serif;
    font-weight: 700;
    font-size: 27px;
    fill: var(--abv-red);
  }
  .strapline {
    font-family: "Rubik", Arial, sans-serif;
    font-weight: 700;
    font-size: 27px;
    letter-spacing: 1px;
  }
  .strapline--top { fill: var(--strap-green); }
  .strapline--bottom { fill: var(--strap-cream); }
</style>
</head>
<body>
<svg class="label" viewBox="0 0 739 1200" xmlns="http://www.w3.org/2000/svg">
  <defs>
    <linearGradient id="scene-tones" x1="0" y1="0" x2="0" y2="1">
      <stop offset="0" stop-color="var(--sky-top)"/>
      <stop offset="0.45" stop-color="var(--sky-mid)"/>
      <stop offset="0.72" stop-color="var(--town)"/>
      <stop offset="0.8" stop-color="var(--water)"/>
      <stop offset="1" stop-color="var(--water-deep)"/>
    </linearGradient>
    <path id="arc-top" d="M 87 640 A 282 472 0 0 1 651 595"/>
    <path id="arc-bottom" d="M 51 595 A 318 508 0 0 0 687 595"/>
  </defs>

  <!-- outer label band -->
  <ellipse class="band" cx="369" cy="595" rx="340" ry="526"/>

  <!-- beach scene area -->
  <ellipse cx="369" cy="595" rx="258" ry="450" fill="url(#scene-tones)"
           role="img" aria-label="Sunset beach scene with palm tree, hotel buildings and sea"/>
  <ellipse class="scene-rim" cx="369" cy="595" rx="258" ry="450"/>

  <!-- straplines on the band -->
  <text class="strapline strapline--top">
    <textPath href="#arc-top" startOffset="2%">Some cheeky strapline about Velvet Dune Glow Beer!</textPath>
  </text>
  <text class="strapline strapline--bottom" text-anchor="middle">
    <textPath href="#arc-bottom" startOffset="50%">something else you want to say about VD Glow</textPath>
  </text>

  <!-- product name -->
  <text class="product-name product-name--large" x="369" y="420" text-anchor="middle">Velvet</text>
  <text class="product-name product-name--large" x="369" y="515" text-anchor="middle">Dune</text>
  <text class="product-name product-name--sub" x="369" y="605" text-anchor="middle">Glow Beer</text>

  <!-- strength -->
  <text class="abv" x="470" y="720" text-anchor="middle">4.5% Alc</text>
</svg>
</body>
</html>
```